Harrowgate Construction And Masonry Ltd

Black background

Logo - attached

Services (bullet points)
New Builds
Extensions
Refurbishments
Alterations
Brickwork Specialists

Contact details - 01632 960418 or 0791 5530274

Email address - contact@harrowgateconstructionandmasonry.co.uk

Website - www.harrowgateconstructionandmasonry.co.uk

Facebook logo

```html
<!DOCTYPE html>
<html lang="en">
<head>
<meta charset="utf-8">
<title>Harrowgate Construction And Masonry Ltd – Flyer</title>
<link href="https://fonts.googleapis.com/css2?family=Kumbh+Sans:wght@400;500;600;700&display=swap" rel="stylesheet">
<style>
  :root {
    --backdrop: #dcdedd;
    --ink: #060606;
    --white: #ffffff;
    --green: #3fba6a;
    --photo-warm: #b89a72;
    --photo-grey: #8d8f8e;
    --photo-light: #d9d6cf;
  }
  * { box-sizing: border-box; margin: 0; padding: 0; }
  html, body { width: 902px; height: 1200px; overflow: hidden; }
  body {
    background: var(--backdrop);
    font-family: "Kumbh Sans", sans-serif;
    position: relative;
  }
  .flyer {
    position: absolute;
    left: 41px; top: 20px;
    width: 820px; height: 1160px;
    background: var(--ink);
    color: var(--white);
    overflow: hidden;
  }
  .brand {
    position: absolute; left: 60px; top: 50px;
    display: flex; align-items: center; gap: 12px;
  }
  .brand-mark { width: 34px; height: 34px; background: var(--green); }
  .brand-name {
    font-weight: 700; font-size: 17px; line-height: 1.2;
    color: var(--white); letter-spacing: 0.5px;
  }
  .headline {
    position: absolute; left: 58px; top: 262px;
    font-weight: 700; font-size: 66px; line-height: 72px;
    letter-spacing: -0.5px;
  }
  .headline .accent { color: var(--green); }
  .intro {
    position: absolute; left: 60px; top: 510px; width: 470px;
    font-weight: 500; font-size: 14px; line-height: 22.5px;
  }
  .services-tag {
    position: absolute; left: 60px; top: 667px;
    width: 214px; height: 38px;
    background: var(--green);
    border-radius: 22px 6px 0 22px;
    font-weight: 600; font-size: 27px; line-height: 38px;
    padding-left: 21px;
  }
  .services {
    position: absolute; left: 70px; top: 718px;
    list-style: none;
  }
  .services li {
    display: flex; align-items: center; gap: 13px;
    font-weight: 600; font-size: 25px; line-height: 30.7px;
  }
  .services svg { width: 20px; height: 20px; flex: none; }
  .call-tag {
    position: absolute; left: 75px; top: 953px;
    width: 142px; height: 23px;
    background: var(--green);
    border-radius: 10px 4px 0 10px;
    font-weight: 500; font-size: 12px; line-height: 23px;
    padding-left: 11px;
  }
  .phones {
    position: absolute; left: 74px; top: 980px;
    font-weight: 600; font-size: 28px; line-height: 31px; letter-spacing: 1px;
  }
  .contact {
    position: absolute; left: 75px; top: 1056px;
    list-style: none; font-size: 12px; font-weight: 500;
  }
  .contact li { display: flex; align-items: center; gap: 4px; height: 24px; }
  .contact svg { width: 16px; height: 16px; flex: none; }
  .social { position: absolute; left: 432px; top: 1080px; display: flex; gap: 10px; }
  .social span { width: 24px; height: 24px; border-radius: 50%; background: var(--green); }
  .snapshot {
    position: absolute; background: var(--white); padding: 10px;
    box-shadow: 0 3px 10px rgba(0,0,0,0.45);
  }
  .snapshot .fill { width: 100%; height: 100%; }
  .snapshot-kitchen { left: 578px; top: 588px; width: 182px; height: 204px; transform: rotate(14deg); }
  .snapshot-kitchen .fill { background: linear-gradient(170deg, var(--photo-light), var(--photo-grey) 60%, var(--photo-warm)); }
  .snapshot-roof { left: 490px; top: 730px; width: 186px; height: 190px; transform: rotate(-8deg); }
  .snapshot-roof .fill { background: linear-gradient(160deg, #8fb4dc, var(--photo-warm) 45%, #caa56c); }
  .snapshot-openplan { left: 508px; top: 892px; width: 232px; height: 206px; transform: rotate(8deg); }
  .snapshot-openplan .fill { background: linear-gradient(175deg, #e7e6e2, #b5b3ad 55%, #7a5a3f); }
</style>
</head>
<body>
  <main class="flyer">
    <div class="brand">
      <span class="brand-mark"></span>
      <p class="brand-name">Harrowgate Construction<br>And Masonry Ltd</p>
    </div>

    <h1 class="headline">Building<br>and Brickwork<br><span class="accent">Specialist’s</span></h1>

    <p class="intro">Harrowgate Construction and Masonry offer the complete building service with over 15 years experience working throughout Cambridgeshire with local home owners looking to improve and add value to their properties.</p>

    <div class="services-tag">SERVICES</div>
    <ul class="services">
      <li><svg viewBox="0 0 20 20"><rect x="1.5" y="3.5" width="15" height="15" rx="3" fill="none" stroke="#3fba6a" stroke-width="2"/><path d="M5 10.5l3.5 3.5L18 3" fill="none" stroke="#3fba6a" stroke-width="2.4" stroke-linecap="round"/></svg>New Builds</li>
      <li><svg viewBox="0 0 20 20"><rect x="1.5" y="3.5" width="15" height="15" rx="3" fill="none" stroke="#3fba6a" stroke-width="2"/><path d="M5 10.5l3.5 3.5L18 3" fill="none" stroke="#3fba6a" stroke-width="2.4" stroke-linecap="round"/></svg>Extensions</li>
      <li><svg viewBox="0 0 20 20"><rect x="1.5" y="3.5" width="15" height="15" rx="3" fill="none" stroke="#3fba6a" stroke-width="2"/><path d="M5 10.5l3.5 3.5L18 3" fill="none" stroke="#3fba6a" stroke-width="2.4" stroke-linecap="round"/></svg>Refurbishments</li>
      <li><svg viewBox="0 0 20 20"><rect x="1.5" y="3.5" width="15" height="15" rx="3" fill="none" stroke="#3fba6a" stroke-width="2"/><path d="M5 10.5l3.5 3.5L18 3" fill="none" stroke="#3fba6a" stroke-width="2.4" stroke-linecap="round"/></svg>Alterations</li>
      <li><svg viewBox="0 0 20 20"><rect x="1.5" y="3.5" width="15" height="15" rx="3" fill="none" stroke="#3fba6a" stroke-width="2"/><path d="M5 10.5l3.5 3.5L18 3" fill="none" stroke="#3fba6a" stroke-width="2.4" stroke-linecap="round"/></svg>Brickwork Specialists</li>
    </ul>

    <div class="call-tag">CALL NOW TODAY!</div>
    <p class="phones">01632 960418<br>0791 5530274</p>

    <ul class="contact">
      <li><svg viewBox="0 0 16 16"><rect x="1.5" y="3.5" width="13" height="9" rx="1.5" fill="none" stroke="#3fba6a" stroke-width="1.3"/><path d="M2 4.5l6 4.5 6-4.5" fill="none" stroke="#3fba6a" stroke-width="1.3"/></svg>contact@harrowgateconstructionandmasonry.co.uk</li>
      <li><svg viewBox="0 0 16 16"><circle cx="8" cy="8" r="6.5" fill="none" stroke="#3fba6a" stroke-width="1.2"/><ellipse cx="8" cy="8" rx="3" ry="6.5" fill="none" stroke="#3fba6a" stroke-width="1.2"/><path d="M1.5 8h13" stroke="#3fba6a" stroke-width="1.2"/></svg>www.harrowgateconstructionandmasonry.co.uk</li>
    </ul>

    <div class="social"><span></span><span></span></div>

    <figure class="snapshot snapshot-kitchen"><div class="fill" role="img" aria-label="Photo of a finished grey shaker kitchen with pendant lights"></div></figure>
    <figure class="snapshot snapshot-roof"><div class="fill" role="img" aria-label="Photo of timber roof rafters under construction against a blue sky"></div></figure>
    <figure class="snapshot snapshot-openplan"><div class="fill" role="img" aria-label="Photo of an open-plan kitchen extension with roof lights and a brick chimney"></div></figure>
  </main>
</body>
</html>
```